Brivel Metrics New Website for Health Benefits Plan Decisioneering Tool Launch

Brivel Metrics is a SaaS provider of health benefits comparison tools. We need a new simple SaaS focused website to direct customers to our product

Target Market(s)

General Public comparing their health benefits plans from their employer or from the state exchanges in the US

Coding

Coded - Design and coding required

Number of Pages Required

3 page

Requirements
Must have
• Main page - "Know the Best Health Benefits Plan for You!"
Graphic of a person looking over papers on their desk
Compare Now button to link to SaaS product
About Us
Product Page

https://plovix.example/top-cloud-sites/

```html
<!DOCTYPE html>
<html lang="en">
<head>
<meta charset="UTF-8">
<title>Brivel Metrics – Health Benefits Plan Comparison</title>
<link rel="stylesheet" href="https://fonts.googleapis.com/css2?family=Cinzel:wght@400;600&family=Lato:wght@400;700&display=swap">
<style>
:root{
  --blue:#2b8fd6;
  --blue-dark:#1f7cc2;
  --sky:#c9e4f4;
  --sky-soft:#e4f2fa;
  --ink:#222226;
  --night:#2b2b2e;
  --mist:#e6e6e8;
  --text:#7b7b7b;
  --white:#ffffff;
}
*{box-sizing:border-box;margin:0;padding:0}
html,body{width:1200px;height:3659px;overflow:hidden}
body{position:relative;background:var(--white);font-family:"Lato",sans-serif;color:var(--text)}
.abs{position:absolute}
.heading{font-family:"Cinzel",serif;font-weight:400;color:var(--ink);font-variant:small-caps;letter-spacing:1px}
.btn{position:absolute;display:flex;align-items:center;justify-content:center;gap:7px;background:var(--blue);color:var(--white);border-radius:24px;font-family:"Lato",sans-serif;font-weight:700;text-transform:uppercase;text-decoration:none}
.btn .arrow{width:12px;height:12px;border-radius:50%;background:var(--white);display:inline-flex;align-items:center;justify-content:center}
.btn .arrow::after{content:"";width:0;height:0;border-left:5px solid var(--blue);border-top:3px solid transparent;border-bottom:3px solid transparent;margin-left:1px}

/* hero */
.hero-photo{position:absolute;left:0;top:0;width:1200px;height:740px;background:linear-gradient(90deg,#ececec 0%,#e2e2e2 35%,#a9b3bd 58%,#6f8193 78%,#4d5a66 100%)}
.brand{position:absolute;font-family:"Cinzel",serif;font-weight:400;color:var(--blue);letter-spacing:1px;white-space:nowrap}
.brand-top{left:145px;top:30px;font-size:30px}
.menu{position:absolute;left:1012px;top:29px;width:44px;height:44px;border-radius:50%;background:var(--blue);display:flex;flex-direction:column;justify-content:center;align-items:center;gap:4px}
.menu span{width:20px;height:3px;background:var(--white);border-radius:2px}
.hero-title{left:145px;top:214px;font-size:50px;line-height:54px}
.hero-btn{left:145px;top:419px;width:180px;height:46px;font-size:14px}
.dots{left:146px;top:540px;display:flex;gap:9px}
.dots i{width:8px;height:8px;border-radius:50%;background:#9a9a9a}
.dots i.on{background:var(--blue)}
.wave{left:0;top:590px}

/* about */
.about-art{left:116px;top:809px;width:438px;height:362px;background:radial-gradient(ellipse at 50% 55%,#d8ecf8 0%,#eef6fb 55%,#ffffff 80%)}
.about-title{left:611px;top:808px;font-size:48px}
.about-copy{left:611px;top:889px;width:460px;font-size:13px;line-height:26.4px}
.about-btn{left:611px;top:1129px;width:156px;height:47px;font-size:14px}

/* products */
.products-bg{left:0;top:1260px}
.products-title{left:0;width:1200px;text-align:center;top:1402px;font-size:48px}
.card{position:absolute;width:217px;height:248px;background:var(--white);box-shadow:0 2px 8px rgba(0,0,0,.1);text-align:center}
.card svg{margin-top:14px}
.card h3{font-family:"Lato",sans-serif;font-weight:400;font-size:16px;color:var(--ink);margin-top:14px}
.card p{font-size:11.5px;line-height:19px;color:var(--text);padding:0 20px;margin-top:14px}
.card .btn{left:44px;top:229px;width:128px;height:38px;font-size:11.5px}
.nav-arrow{position:absolute;width:44px;height:44px;border-radius:50%;border:2px solid #5a5a5a;display:flex;align-items:center;justify-content:center}

/* news */
.news-title{left:0;width:1200px;text-align:center;top:2077px;font-size:48px}
.news-feature{left:145px;top:2200px;width:368px;height:421px;background:var(--white);box-shadow:0 2px 10px rgba(0,0,0,.15)}
.news-photo{position:absolute;left:7px;top:8px;width:354px;height:192px;background:linear-gradient(135deg,#c9b89c 0%,#d9d4cc 40%,#6f7d8a 75%,#3d4650 100%)}
.date{position:absolute;width:73px;height:81px;background:var(--blue);color:var(--white);font-weight:700;font-size:20px;line-height:24px;display:flex;flex-direction:column;align-items:center;justify-content:center}
.news-feature .date{left:7px;top:207px}
.news-feature h4{position:absolute;left:106px;top:220px;width:240px;font-size:17px;line-height:25px;font-weight:400;color:var(--ink)}
.news-feature p{position:absolute;left:108px;top:282px;width:240px;font-size:11.5px;line-height:18.5px}
.news-feature a{position:absolute;left:106px;top:384px;font-weight:700;font-size:15px;color:var(--blue);text-decoration:none}
.news-item{position:absolute;left:534px;width:524px;height:129px;border:1px solid #dedede;background:var(--white)}
.news-item .date{left:8px;top:8px}
.news-item h4{position:absolute;left:108px;top:18px;font-size:17px;font-weight:400;color:var(--ink)}
.news-item p{position:absolute;left:108px;top:52px;width:390px;font-size:11px;line-height:18.5px}

/* contact */
.contact-bg{left:0;top:2670px}
.contact-title{left:0;width:1200px;text-align:center;top:2851px;font-size:48px;color:var(--white)}
.field{position:absolute;background:var(--white);font-size:13px;color:#6a6a6a;padding:0 21px;display:flex;align-items:center}
.field.msg{align-items:flex-start;padding-top:19px}
.submit{left:523px;top:3240px;width:154px;height:46px;font-size:14px}

/* footer */
.brand-foot{left:142px;top:3522px;font-size:38px}
.social{left:524px;top:3495px;display:flex;gap:9px}
.social i{width:37px;height:37px;border-radius:50%;border:2px solid var(--blue)}
.footer-nav{left:523px;top:3553px;font-size:16px;color:var(--ink);display:flex;gap:16px;white-space:nowrap}
.footer-nav span.sep{color:var(--ink)}
.copyright{left:523px;top:3596px;font-size:11px;color:#555}
</style>
</head>
<body>

<!-- Hero -->
<div class="hero-photo" role="img" aria-label="Photo of a smiling man at his desk looking over papers in a bright office"></div>
<div class="brand brand-top">Brivel Metrics</div>
<div class="menu"><span></span><span></span><span></span></div>
<h1 class="abs heading hero-title">Know the Best<br>Health Benefits<br>Plan for You!</h1>
<a class="btn hero-btn" href="#">Compare Now <span class="arrow"></span></a>
<div class="abs dots"><i></i><i></i><i class="on"></i><i></i><i></i></div>
<svg class="abs wave" width="1200" height="150" viewBox="0 0 1200 150">
  <path d="M0 70 C150 30 360 10 538 50 L600 128 L662 50 C840 10 1050 30 1200 70 L1200 150 L0 150 Z" fill="#ffffff"/>
  <path d="M0 70 C150 30 360 10 538 50 L600 128 L662 50 C840 10 1050 30 1200 70" fill="none" stroke="#2b8fd6" stroke-width="9"/>
</svg>

<!-- About -->
<div class="abs about-art" role="img" aria-label="Illustration of cloud SaaS connected to a desktop, phone and laptop"></div>
<h2 class="abs heading about-title">About Us</h2>
<p class="abs about-copy">Lorem ipsum dolor sit amet, consectetur adipiscing elit, sed do eiusmod tempor incididunt ut labore et dolore magna aliqpsum suspendisse ultrices gravommodo viverra maecenas accumsan lacus vel facilisis. Lorem ipsum dolor sit amet, consectetur adipiscing elit, sed do eiusmod tempor incididunt ut labore et dolore magna aliqpsum suspendisse ultrices gravommodo viverra maecenas accumsan lacus vel facilisis. Lorem ipsum dolor sit amet, consectetur adipiscing elit, sed do eiusmod tempor incididunt ut labore et dolore magna aliqpsum</p>
<a class="btn about-btn" href="#">Read More <span class="arrow"></span></a>

<!-- Featured products -->
<svg class="abs products-bg" width="1200" height="760" viewBox="0 0 1200 760">
  <ellipse cx="640" cy="378" rx="940" ry="366" fill="#e4f2fa"/>
  <ellipse cx="600" cy="376" rx="860" ry="338" fill="#c9e4f4"/>
</svg>
<h2 class="abs heading products-title">Featured Products</h2>

<div class="nav-arrow" style="left:76px;top:1661px"><svg width="14" height="18"><path d="M10 2 L3 9 L10 16" fill="none" stroke="#4a4a4a" stroke-width="2"/></svg></div>
<div class="nav-arrow" style="left:1080px;top:1661px"><svg width="14" height="18"><path d="M4 2 L11 9 L4 16" fill="none" stroke="#4a4a4a" stroke-width="2"/></svg></div>

<div class="card" style="left:145px;top:1536px">
  <svg width="60" height="58" viewBox="0 0 60 58" fill="none" stroke="#333" stroke-width="1.6"><path d="M14 30 a10 10 0 0 1 4-19 a13 13 0 0 1 25 2 a9 9 0 0 1 2 17"/><rect x="12" y="32" width="28" height="18"/><path d="M8 53 H44"/><rect x="44" y="30" width="10" height="20" rx="2"/></svg>
  <h3>PRODUCT NAME</h3>
  <p>Lorem ipsum dolor sit amet, consectetur adipiscing elit, sed do eiusmod tempor incididunt ut labore et dolore magna</p>
  <a class="btn" href="#">Read More <span class="arrow"></span></a>
</div>
<div class="card" style="left:376px;top:1562px">
  <svg width="60" height="58" viewBox="0 0 60 58" fill="none" stroke="#333" stroke-width="1.6"><path d="M14 36 a11 11 0 0 1 3-21 a14 14 0 0 1 27 2 a10 10 0 0 1 1 19 Z"/><circle cx="30" cy="26" r="6"/><path d="M22 44 v8 M30 44 v10 M38 44 v8"/></svg>
  <h3>PRODUCT NAME</h3>
  <p>Lorem ipsum dolor sit amet, consectetur adipiscing elit, sed do eiusmod tempor incididunt ut labore et dolore magna</p>
  <a class="btn" href="#">Read More <span class="arrow"></span></a>
</div>
<div class="card" style="left:608px;top:1536px">
  <svg width="60" height="58" viewBox="0 0 60 58" fill="none" stroke="#333" stroke-width="1.6"><path d="M28 44 L8 24 a10 10 0 0 1 20-12 a10 10 0 0 1 20 10"/><circle cx="42" cy="38" r="11"/><path d="M42 32 v12 M36 38 h12"/></svg>
  <h3>PRODUCT NAME</h3>
  <p>Lorem ipsum dolor sit amet, consectetur adipiscing elit, sed do eiusmod tempor incididunt ut labore et dolore magna</p>
  <a class="btn" href="#">Read More <span class="arrow"></span></a>
</div>
<div class="card" style="left:839px;top:1562px">
  <svg width="60" height="58" viewBox="0 0 60 58" fill="none" stroke="#333" stroke-width="1.6"><rect x="6" y="14" width="42" height="30"/><path d="M22 44 v8 M32 44 v8 M16 53 H38"/><circle cx="42" cy="14" r="9"/><circle cx="42" cy="14" r="3"/><circle cx="22" cy="30" r="6"/></svg>
  <h3>PRODUCT NAME</h3>
  <p>Lorem ipsum dolor sit amet, consectetur adipiscing elit, sed do eiusmod tempor incididunt ut labore et dolore magna</p>
  <a class="btn" href="#">Read More <span class="arrow"></span></a>
</div>

<!-- Latest news -->
<h2 class="abs heading news-title">Latest News</h2>
<article class="abs news-feature">
  <div class="news-photo" role="img" aria-label="Photo of a laptop showing a SaaS chart beside a coffee cup on a desk"></div>
  <div class="date"><span>DEC</span><span>2020</span></div>
  <h4>Nemo enim ipsam voluptatem quia voluptas sit</h4>
  <p>Lorem ipsum dolor sit amet, consectetur adipiscing elit, sed do eiusmod tempor incididunt ut labore et dolore magna alis ipsum suspendisse ultrices s commodo viverra maecenas alacus vel facilisis.</p>
  <a href="#">READ MORE</a>
</article>
<article class="news-item" style="top:2200px">
  <div class="date"><span>DEC</span><span>2020</span></div>
  <h4>Nemo enim ipsam voluptatem quia voluptas sit</h4>
  <p>Lorem ipsum dolor sit amet, consectetur adipiscing elit, sed do eiusmod tempor incididunt ut labore et dolore magna alis ipsum suspendisse ultrices s commodo viverra maecenas alacus vel facilisis.</p>
</article>
<article class="news-item" style="top:2347px">
  <div class="date"><span>DEC</span><span>2020</span></div>
  <h4>Nemo enim ipsam voluptatem quia voluptas sit</h4>
  <p>Lorem ipsum dolor sit amet, consectetur adipiscing elit, sed do eiusmod tempor incididunt ut labore et dolore magna alis ipsum suspendisse ultrices s commodo viverra maecenas alacus vel facilisis.</p>
</article>
<article class="news-item" style="top:2494px">
  <div class="date"><span>DEC</span><span>2020</span></div>
  <h4>Nemo enim ipsam voluptatem quia voluptas sit</h4>
  <p>Lorem ipsum dolor sit amet, consectetur adipiscing elit, sed do eiusmod tempor incididunt ut labore et dolore magna alis ipsum suspendisse ultrices s commodo viverra maecenas alacus vel facilisis.</p>
</article>

<!-- Contact -->
<svg class="abs contact-bg" width="1200" height="790" viewBox="0 0 1200 790">
  <ellipse cx="560" cy="392" rx="880" ry="378" fill="#e6e6e8"/>
  <ellipse cx="600" cy="408" rx="840" ry="338" fill="#2b2b2e"/>
</svg>
<h2 class="abs heading contact-title">Contact Form</h2>
<div class="field" style="left:234px;top:2963px;width:360px;height:52px">First Name</div>
<div class="field" style="left:605px;top:2963px;width:361px;height:52px">Last Name</div>
<div class="field" style="left:234px;top:3027px;width:360px;height:53px">Email address</div>
<div class="field" style="left:605px;top:3027px;width:361px;height:53px">Phone Number</div>
<div class="field msg" style="left:234px;top:3093px;width:732px;height:113px">Message</div>
<a class="btn submit" href="#">Submit <span class="arrow"></span></a>

<!-- Footer -->
<div class="brand brand-foot">Brivel Metrics</div>
<div class="abs social"><i></i><i></i><i></i><i></i></div>
<nav class="abs footer-nav"><span>HOME</span><span class="sep">/</span><span>ABOUT US</span><span class="sep">/</span><span>PRODUCTS</span><span class="sep">/</span><span>NEWS</span><span class="sep">/</span><span>CONTACT US</span></nav>
<p class="abs copyright">Copyrights @ 2020 Brivel Metrics. All Rights Reserved &nbsp;|&nbsp; Privacy Policy &nbsp;|&nbsp; Terms and Use</p>

</body>
</html>
```